Web Design for non-profit, Nautical themed

We are developing a web design for a non-profit organization. They are:

a non-profit 501©3 educational and service organization, grounded in the recognition that active engagement of the arts through can be an entry into growth and transformation. Our purpose is to develop and offer events that support this creative process bringing outstanding presenters to our town.

They are located in a beautiful coastal town and the client would like a "nautical" theme. This would include

- color palette of blue, green, possibly brown/beige, and possibly some deep red colors as accents. There is a file attached with some color palette ideas, but you don't have to choose from colors here.

- soothing, calm, clean professional look

- something in the background image that would indicate the four directions. This could be a compass or something similar.

- the client really likes this website:
http://www.harbrowcollective.example/

Please see attached for:

- a basic sketch that shows the overall layout that we desire. Feel free to modify this slightly but not too much. File name is 01-sketch.psd

- placeholder content that can be used throughout your design

You can also use any of the stock photos found here:
http://www.pellumimages.example/search/lightbox/48207356#b9a2d71

Target Market(s)

Mainly white American women who are in their 40s or older. Professional, affluent, highly educated.

Industry/Entity Type

Nautical

Requirements
Must have
• - sidebar with event information. Each event should include date, headshot, title, brief description and a "Register" and "Read more" link. We don't have any real headshots so use ones from Internet for now.

- use the attached 01-sketch.psd file as your starting point.

```html
<!DOCTYPE html>
<html lang="en">
<head>
<meta charset="utf-8">
<title>Tidewater Dialogues Inc.</title>
<link href="https://fonts.googleapis.com/css2?family=PT+Sans+Narrow:wght@400;700&family=Source+Sans+3:wght@400;600&display=swap" rel="stylesheet">
<style>
:root{
  --navy:#1e4a66;
  --navy-dark:#143449;
  --navy-light:#2a6184;
  --sidebar:#1d4a5f;
  --sidebar-band:#2b5e73;
  --sea:#2f7f78;
  --sea-dark:#1f5d58;
  --sea-light:#3f9a90;
  --accent:#8e2f3f;
  --sand:#efe6d2;
  --ink:#3a3a3a;
  --footer:#23323b;
  --footer-text:#d3dbe0;
  --foam:#74c6b8;
  --head:"PT Sans Narrow", "Arial Narrow", sans-serif;
  --body:"Source Sans 3", Arial, sans-serif;
}
*{box-sizing:border-box;margin:0;padding:0}
html,body{width:1200px;height:1192px;overflow:hidden}
body{position:relative;font-family:var(--body);color:var(--ink);
  background:linear-gradient(#e3e9ec 0,#f7fafb 50px,#ffffff 200px,#ffffff 100%)}
.abs{position:absolute}

/* compass rose background */
.compass{left:860px;top:52px;width:170px;height:170px;opacity:.16}

/* navigation */
.main-nav{left:117px;top:0;width:962px;height:51px;display:flex;
  background:linear-gradient(var(--navy-light),var(--navy-dark));box-shadow:0 2px 3px rgba(0,0,0,.25);border-radius:0 0 3px 3px}
.main-nav a{font-family:var(--head);font-size:17px;color:#fff;text-decoration:none;
  display:flex;align-items:center;justify-content:center;border-right:1px solid rgba(0,0,0,.2);
  box-shadow:inset -1px 0 0 rgba(255,255,255,.08)}
.main-nav a.active{background:linear-gradient(#a4a4a4,#7c7c7c)}
.main-nav a:last-child{border-right:none}

/* brand */
.brand{left:120px;top:70px;display:flex;align-items:center;gap:14px}
.brand-mark{width:64px;height:64px;border-radius:50%;background:#555}
.brand-name{font-family:var(--body);font-weight:400;font-size:42px;line-height:44px;color:#4a4a4a;width:360px}

/* sidebar */
.sidebar{left:106px;top:209px;width:293px;height:752px;background:var(--sidebar);
  border:2px solid #d6e0e5;border-radius:3px;box-shadow:0 0 3px rgba(0,0,0,.2);overflow:hidden}
.social-row{position:absolute;left:22px;top:22px;display:flex;gap:5px}
.social-row span{width:30px;height:30px;border-radius:50%;background:var(--sand);box-shadow:0 1px 2px rgba(0,0,0,.3)}
.mailing{position:absolute;left:0;top:63px;width:100%;height:106px;background:var(--sidebar-band)}
.side-title{font-family:var(--head);color:#fff;font-size:17px}
.mailing .side-title{position:absolute;left:22px;top:14px}
.mailing input{position:absolute;left:14px;top:55px;width:179px;height:27px;border:1px solid #ccc;background:#fff}
.join-btn{position:absolute;left:198px;top:52px;width:83px;height:34px;border-radius:6px;
  background:linear-gradient(#5a5a5a,#2e2e2e);color:#fff;font-family:var(--head);font-size:20px;
  display:flex;align-items:center;justify-content:center}
.events-head{position:absolute;left:0;top:170px;width:100%;height:59px;border-bottom:1px solid rgba(255,255,255,.15)}
.events-head .side-title{position:absolute;left:12px;top:18px;font-size:20px}
.pager{position:absolute;top:28px;width:20px;height:20px;border-radius:50%;background:#d5d5d5;
  display:flex;align-items:center;justify-content:center}
.pager svg{width:8px;height:8px}
.event{position:absolute;left:0;width:100%}
.headshot{position:absolute;left:9px;width:91px;border:1px solid #4f7d90;
  background:linear-gradient(#8a7a6e,#6b5446)}
.event-info{position:absolute;left:107px;width:178px;color:#fff}
.event-title{font-size:14.5px;line-height:20px}
.event-meta{font-size:12.5px;line-height:20.5px}
.event-desc{font-size:11px;line-height:16px;color:#dbe8ee;margin-top:1px}
.event-btn{position:absolute;width:96px;height:33px;border-radius:3px;color:#fff;
  font-family:var(--head);font-size:15px;display:flex;align-items:center;justify-content:center;
  background:linear-gradient(var(--sea-light),var(--sea-dark));box-shadow:0 1px 2px rgba(0,0,0,.35)}
.event-btn.read{background:linear-gradient(var(--sea-light),#173f3c 60%,var(--sea-dark))}
.event-divider{position:absolute;left:0;width:100%;height:1px;background:rgba(255,255,255,.15)}

/* slider */
.slider{left:423px;top:210px;width:654px;height:314px;border:3px solid #9a9a9a;overflow:hidden;
  background:linear-gradient(160deg,#cfe0ef 0%,#9ec2e2 40%,#b5804d 62%,#a0642f 80%,#d9c6ad 100%)}
.slider-caption{position:absolute;left:0;bottom:0;width:100%;height:45px;background:rgba(40,40,40,.75);
  color:#fff;font-family:var(--head);font-size:16.5px;display:flex;align-items:center;justify-content:center}
.slider-arrow{position:absolute;top:133px;width:20px;height:39px;background:#222;display:flex;align-items:center;justify-content:center}

/* intro */
.intro-title{left:425px;top:554px;font-family:var(--head);font-weight:400;font-size:23px;color:#3c3c3c;
  padding-bottom:5px;border-bottom:1px dotted #777}
.intro-title em{font-style:normal;color:var(--navy)}
.intro-text{left:429px;top:603px;width:635px;font-size:12.5px;line-height:21px;color:#555}

/* feature cards */
.card{top:674px;width:206px;height:288px;border:2px solid #e0e0e0;border-radius:3px;
  background:linear-gradient(#fbfbfb,#e4e4e4);box-shadow:inset 0 0 0 1px #fff,0 0 3px rgba(0,0,0,.12)}
.card h2{position:absolute;left:24px;top:15px;font-family:var(--head);font-weight:400;font-size:20px;color:var(--navy-dark)}
.card p{position:absolute;left:15px;top:49px;width:176px;font-size:11.6px;line-height:16px;color:#333}
.card p a{color:var(--sea);text-decoration:none}
.card .more{position:absolute;right:14px;top:238px;width:119px;height:28px;border-radius:3px;background:var(--navy);
  color:#fff;font-family:var(--head);font-size:16px;display:flex;align-items:center;justify-content:center}

/* footer */
.site-footer{left:0;top:994px;width:1200px;height:198px;background:var(--footer);border-top:3px solid #152027}
.foot-title{position:absolute;font-family:var(--head);font-size:23px;color:var(--foam);top:11px}
.sitemap{position:absolute;left:124px;top:49px;list-style:none}
.sitemap li{font-size:13px;line-height:21px;color:var(--footer-text)}
.sitemap li::before{content:"›";margin-right:9px;color:#fff}
.contact{position:absolute;left:451px;top:51px;width:235px;font-size:13px;line-height:16px;color:var(--footer-text)}
.contact p{margin-bottom:5px}
.foot-social{position:absolute;left:948px;top:28px;display:flex;gap:5px}
.foot-social span{width:22px;height:22px;border-radius:3px;background:#5a8fc8}
.foot-social span:nth-child(3){background:#e88b2c}
.foot-social span:nth-child(5){background:#c33}
.copyright{position:absolute;right:119px;top:66px;font-size:12px;color:#fff}
</style>
</head>
<body>

<svg class="compass abs" viewBox="-100 -100 200 200" aria-hidden="true">
  <g fill="none" stroke="#1e4a66" stroke-width="2">
    <circle r="92"/><circle r="80"/><circle r="30"/>
    <line x1="-100" y1="0" x2="100" y2="0"/><line x1="0" y1="-100" x2="0" y2="100"/>
    <line x1="-65" y1="-65" x2="65" y2="65"/><line x1="-65" y1="65" x2="65" y2="-65"/>
  </g>
  <g fill="#1e4a66">
    <polygon points="0,-88 10,-10 0,0 -10,-10"/><polygon points="0,88 10,10 0,0 -10,10"/>
    <polygon points="88,0 10,10 0,0 10,-10"/><polygon points="-88,0 -10,10 0,0 -10,-10"/>
  </g>
</svg>

<nav class="main-nav abs">
  <a class="active" style="width:141px" href="#">HOME</a>
  <a style="width:130px" href="#">CALENDAR</a>
  <a style="width:141px" href="#">ABOUT US</a>
  <a style="width:130px" href="#">DONATE</a>
  <a style="width:207px" href="#">TRAVEL INFORMATION</a>
  <a style="width:213px" href="#">CONTACT US</a>
</nav>

<div class="brand abs">
  <span class="brand-mark"></span>
  <span class="brand-name">Tidewater Dialogues Inc.</span>
</div>

<aside class="sidebar abs">
  <div class="social-row"><span></span><span></span><span></span><span></span><span></span><span></span></div>
  <div class="mailing">
    <div class="side-title">JOIN OUR MAILING LIST</div>
    <input type="text" aria-label="Email address">
    <div class="join-btn">JOIN</div>
  </div>
  <div class="events-head">
    <div class="side-title">UPCOMING EVENTS</div>
    <span class="pager" style="left:226px"><svg viewBox="0 0 8 8"><path d="M6 0 2 4 6 8" fill="none" stroke="#333" stroke-width="1.6"/></svg></span>
    <span class="pager" style="left:257px"><svg viewBox="0 0 8 8"><path d="M2 0 6 4 2 8" fill="none" stroke="#333" stroke-width="1.6"/></svg></span>
  </div>

  <div class="event" style="top:251px">
    <div class="headshot" role="img" aria-label="Headshot of the workshop presenter" style="top:0;height:137px"></div>
    <div class="event-info" style="top:-3px">
      <div class="event-title">Starting Close InPresenters</div>
      <div class="event-meta">Date : May 28, 2013</div>
      <div class="event-meta">Faculty: Marion &amp; Kelsey</div>
      <div class="event-meta">Description &nbsp;:</div>
      <div class="event-desc">Heeding the implicit wisdom in R.M. Halloway's line "We had the experience but missed the meaning," this concluding workshop</div>
    </div>
    <div class="event-btn" style="left:38px;top:161px">REGISTER</div>
    <div class="event-btn read" style="left:159px;top:161px">READ MORE</div>
  </div>
  <div class="event-divider" style="top:477px"></div>

  <div class="event" style="top:510px">
    <div class="headshot" role="img" aria-label="Headshot of the naturalist presenter" style="top:0;height:146px"></div>
    <div class="event-info" style="top:-4px">
      <div class="event-title">Delighting in Nature</div>
      <div class="event-meta">Date : May 28, 2013</div>
      <div class="event-meta">Faculty: Peter Lindqvist</div>
      <div class="event-meta">Description &nbsp;:</div>
      <div class="event-desc">Join local naturalist and marine biologist on an invigorating and rejuvenating morning nature walk amidst the flora and fauna of beautiful Camp Merrow.</div>
    </div>
    <div class="event-btn" style="left:38px;top:181px">REGISTER</div>
    <div class="event-btn read" style="left:159px;top:181px">READ MORE</div>
  </div>
</aside>

<section class="slider abs" role="img" aria-label="Photo of a wooden ship's wheel against a blue sky with rigging">
  <span class="slider-arrow" style="left:0"><svg width="6" height="8" viewBox="0 0 6 8"><path d="M5 0 1 4 5 8" fill="none" stroke="#fff" stroke-width="1.4"/></svg></span>
  <span class="slider-arrow" style="right:3px"><svg width="6" height="8" viewBox="0 0 6 8"><path d="M1 0 5 4 1 8" fill="none" stroke="#fff" stroke-width="1.4"/></svg></span>
  <div class="slider-caption">Ut blandit, turpis non interdum tincidunt, libero augue pretium libero, in vehicula quam.</div>
</section>

<h1 class="intro-title abs">Conversations that Could <em>Transform Your Life</em></h1>
<p class="intro-text abs">Tidewater Dialogues is bringing together speakers from around the globe who are transforming our world. Join us for an event that could change your life.</p>

<article class="card abs" style="left:423px">
  <h2>ABOUT US</h2>
  <p>Tidewater Dialogues Inc. is a non-profit 501©3 educational and service organization, grounded in the recognition that active engagement of the arts through can be an entry into growth and transformation. Our purpose is to develop and offer events that support this creative process bringing outstanding presenters into the Calder Bay, Maryland area.</p>
  <span class="more">Read More</span>
</article>
<article class="card abs" style="left:651px">
  <h2>HOW YOU CAN HELP</h2>
  <p style="top:52px">Interested in volunteering for Tidewater Dialogues? &nbsp;Please send an email to <a href="#">info@tidewaterdialogues.org</a> detailing your interest, preferred time commitment (i.e. helping with an event for an afternoon or evening, monthly meetings, etc.) and skills or services that you may offer.</p>
  <span class="more">Read More</span>
</article>
<article class="card abs" style="left:881px">
  <h2>OUR SPEAKERES</h2>
  <p>Tidewater Dialogues Inc. is a non-profit 501©3 educational and service organization, grounded in the recognition that active engagement of the arts through can be an entry into growth and transformation. Our purpose is to develop and offer events that support this creative process bringing outstanding presenters into the Calder Bay, Maryland area.</p>
  <span class="more">Read More</span>
</article>

<footer class="site-footer abs">
  <div class="foot-title" style="left:120px">SITEMAP</div>
  <ul class="sitemap">
    <li>Home</li><li>Calendar</li><li>About Us</li><li>Donate</li><li>Travel Information</li><li>Contact</li>
  </ul>
  <div class="foot-title" style="left:441px">CONTACT US</div>
  <div class="contact">
    <p>Address :</p>
    <p style="margin-top:6px;margin-bottom:13px">Nunc varius facilisis eros. Sed erat. In in velit quis arcu ornare laoreet. Nunc varius facilisis eros. Sed erat.</p>
    <p>Phone Number ; 236 510 204</p>
    <p>Email : info@tidewaterdialogues.inc</p>
  </div>
  <div class="foot-social"><span></span><span></span><span></span><span></span><span></span></div>
  <div class="copyright">© &nbsp;2013 &nbsp;tidewaterdialogues.inc. All rights reserved.</div>
</footer>

</body>
</html>
```